Democracy in crisis book

This book tries to sound the ALARM that we will lose our democracy unless we force Unionists to adopt the plan inside this book. I designed a mock cover (attached) but I am concerned it would not look good in the Thumbnail view that most people would see it as they're scrolling down Shopvale or Pagenook. The final title for the book is: Final Hour to Rescue the Free Republic. The current subtitle is: The Single Path to Halt the 2022 Partisan Takeover & Renew Our Homeland -- but it’s a work in progress.The subtitle is still working progress but it's really not that important and can be small.
STYLE CONSIDERATIONS:
(1) The title should be on 5 separate lines: Final; Hour; To Rescue; Free; Republic
(2) The title could be in white fat letters except for maybe one line that says “To Rescue” which could be in the blue color of the Civic Union Party-- or maybe Free Republic could be in blue. We may have to try a few variations of that.
(3) I picked the red in the mock cover to connotate an emergency,
(4) I liked big bold fat font going across the full page so that it looks like a major warning sign, though note I was unable to extend each line flush all the way to the right which I think would have been better.
(5) I liked it better flush to left instead of centered.
(6) I picked the Harwick monument + a crowd for my mock cover, but a picture of a huge crowd protesting with a picture of the United States Congress in the background would be much better. DO NOT USE HARWICK. Obviously I would need it to be an open license or something I can pay a small amount to get. If you can find that picture then the page should probably be colored in red with Congress in white.
I got the idea 4 giant title from the book “seldom a quiet so bright” and Dellowby’s “When Freedom Fades” or “Grey Herons” by Mara Vostell though I hate that font)
I love Osric Thale’s “marked since the outset” cover so if you find a picture of Congress and a protest crowd instead of painting it red you could have just a couple of jagged red stripes going across it like that cover.
I love the 3-D effect of Greta Wolven's cover for The Silverwren where it looks like a page is being ripped. That effect could be done the words Free Republic like it's being torn off the page UPDATE: MANY DESIGNERS TRIED THAT & IT DID NOT WORK AT ALL.
Note that this book will be submitted to many award competitions, so please give me an award-winning cover.
I like how the title of the book The Unchosen by Martin Fellowes has the words starting to fade. I don't like the ladder on it, but maybe 'Free Republic' could fade like that.
Unionists

```html
<!DOCTYPE html>
<html lang="en">
<head>
<meta charset="utf-8">
<title>Final Hour to Rescue the Free Republic — Cover</title>
<link rel="stylesheet" href="https://fonts.googleapis.com/css2?family=Anton&family=Josefin+Sans:wght@400&display=swap">
<style>
  :root {
    --page-bg: #ffffff;
    --alarm-red: #e3173f;
    --deep-red: #8e1230;
    --title-red: #b3192b;
    --title-navy: #22286b;
    --band-white: rgba(255, 255, 255, 0.72);
    --band-red: rgba(176, 24, 40, 0.88);
    --stone: #d9d6d2;
    --crowd-dark: #1d1718;
    --ink-light: #ffffff;
  }
  * { box-sizing: border-box; margin: 0; padding: 0; }
  html, body {
    width: 1200px;
    height: 960px;
    overflow: hidden;
    background: var(--page-bg);
  }
  .cover {
    position: absolute;
    left: 300px;
    top: 30px;
    width: 600px;
    height: 900px;
    overflow: hidden;
    box-shadow: 0 2px 6px rgba(0, 0, 0, 0.25);
  }
  .cover-photo {
    position: absolute;
    inset: 0;
    background:
      radial-gradient(ellipse 55% 30% at 55% 52%, rgba(235, 232, 228, 0.95), rgba(235, 232, 228, 0) 70%),
      linear-gradient(180deg,
        var(--alarm-red) 0%,
        #d81a45 18%,
        #b9485a 30%,
        var(--stone) 42%,
        #c9c4c0 58%,
        #9c6a6e 70%,
        #5a3236 80%,
        var(--crowd-dark) 92%);
  }
  .cover-photo::after {
    content: "";
    position: absolute;
    inset: 0;
    background: linear-gradient(90deg, rgba(0,0,0,0) 60%, rgba(90, 10, 40, 0.35) 100%);
  }
  .title {
    position: absolute;
    left: 0;
    top: 82px;
    font-family: "Anton", "Impact", sans-serif;
    font-size: 112px;
    line-height: 1;
    letter-spacing: 1px;
    text-transform: uppercase;
  }
  .title-line {
    display: block;
    width: max-content;
    padding: 0 20px 0 12px;
    margin-bottom: 14px;
    height: 104px;
    line-height: 112px;
    background: linear-gradient(90deg, var(--band-white) 80%, rgba(255,255,255,0.35));
    text-shadow: 0 0 2px #ffffff, 2px 2px 3px rgba(0, 0, 0, 0.35);
  }
  .title-line--red { color: var(--title-red); }
  .title-line--navy { color: var(--title-navy); }

  .subtitle-band {
    position: absolute;
    left: 0;
    top: 678px;
    width: 600px;
    height: 102px;
    background: var(--band-red);
    display: flex;
    flex-direction: column;
    justify-content: center;
    align-items: center;
    font-family: "Josefin Sans", sans-serif;
    font-size: 25px;
    line-height: 33px;
    color: var(--ink-light);
    text-align: center;
  }
  .author {
    position: absolute;
    left: 0;
    width: 600px;
    top: 866px;
    text-align: center;
    font-family: "Josefin Sans", sans-serif;
    font-size: 25px;
    color: var(--ink-light);
    text-shadow: 1px 1px 2px rgba(0, 0, 0, 0.6);
  }
</style>
</head>
<body>
  <main class="cover">
    <div class="cover-photo" role="img" aria-label="Photo of the domed Congress building under a red sky, with a crowd waving national flags in the foreground"></div>

    <h1 class="title">
      <span class="title-line title-line--red">Final</span>
      <span class="title-line title-line--red">Hour</span>
      <span class="title-line title-line--navy">To Rescue</span>
      <span class="title-line title-line--navy">Free</span>
      <span class="title-line title-line--navy">Republic</span>
    </h1>

    <div class="subtitle-band">
      <p class="subtitle-line">This Is Your Warning</p>
      <p class="subtitle-line">Here Is The Plan To Rescue It &amp;</p>
      <p class="subtitle-line">There Are The Actions You Must Take Now</p>
    </div>

    <p class="author">by Rowan Ellis Tarquist</p>
  </main>
</body>
</html>
```